Kid's Cancer Camp Business Card

Create a unique Two-Sided color business cards for Camp Willow Brook, a pediatric cancer camp.

The camp tag line is: A camp where brave young hearts find joy...

Dale Morrisey, Executive Director
Camp Willow Brook Charitable Foundation, Inc
PO Box 918
Alder Falls, VT 06832

Phone - 203-555-0143
Fax - 203-555-0187
Email: dale@campwillowbrook.example
www.campwillowbrook.example

Target Market(s)

Potential Donors, Volunteers and Campers

Industry/Entity Type

Non-profit pediatric cancer camp

Contact Information for Business Card

All contact info that is included in the description

Font styles to use
Other font styles liked:
• Designer chooses font

Requirements
Must have
• Camp Willow Brook Logo and Tag Line
Nice to have
• should be eye catching
Should not have
• not cartoony

```html
<!DOCTYPE html>
<html lang="en">
<head>
<meta charset="utf-8">
<title>Camp Willow Brook – Business Card</title>
<link rel="stylesheet" href="https://fonts.googleapis.com/css2?family=Open+Sans:wght@400;600;700&display=swap">
<style>
  :root {
    --backdrop: #e9e4de;
    --card: #252525;
    --teal: #17a19c;
    --brand-blue: #1f63a8;
    --sun: #fbb71f;
    --text: #ffffff;
  }
  * { margin: 0; padding: 0; box-sizing: border-box; }
  html, body {
    width: 1047px; height: 1200px; overflow: hidden;
    background: var(--backdrop);
    font-family: "Open Sans", Arial, sans-serif;
  }
  .canvas { position: relative; width: 1047px; height: 1200px; }
  .card {
    position: absolute; left: 240px; top: 80px;
    width: 567px; height: 1040px;
    background: var(--card);
    border-radius: 24px;
    color: var(--text);
    box-shadow: 0 10px 30px rgba(0,0,0,.18);
  }
  .line { position: absolute; left: 0; width: 100%; text-align: center; white-space: nowrap; }
  .brand-mark {
    position: absolute; left: 50%; top: 100px;
    width: 170px; height: 170px; margin-left: -85px;
    border-radius: 50%; background: var(--sun);
  }
  .brand-name { top: 318px; font-size: 50px; line-height: 64px; font-weight: 600; color: var(--brand-blue); }
  .person-name { top: 398px; font-size: 38px; line-height: 46px; font-weight: 700; color: var(--teal); }
  .person-title { top: 447px; font-size: 23px; line-height: 30px; font-weight: 400; }
  .divider { position: absolute; left: 0; width: 567px; height: 50px; }
  .divider--contact { top: 515px; }
  .divider--address { top: 760px; }
  .contact-list { top: 597px; font-size: 25px; line-height: 35.5px; }
  .address { top: 825px; font-size: 25px; line-height: 34.5px; }
  .tagline { top: 958px; font-size: 25px; line-height: 36px; }
</style>
</head>
<body>
<div class="canvas">
  <div class="card">
    <div class="brand-mark"></div>
    <div class="line brand-name">Camp Willow Brook</div>
    <div class="line person-name">Dale Morrisey</div>
    <div class="line person-title">Executive Director</div>

    <svg class="divider divider--contact" viewBox="0 0 567 50" aria-hidden="true">
      <g stroke="var(--teal)" stroke-width="3" stroke-linecap="round">
        <line x1="38" y1="25" x2="182" y2="25"/>
        <line x1="400" y1="25" x2="536" y2="25"/>
      </g>
      <g fill="var(--teal)">
        <circle cx="219" cy="25" r="21"/><circle cx="267" cy="25" r="21"/>
        <circle cx="314" cy="25" r="21"/><circle cx="363" cy="25" r="21"/>
      </g>
      <path class="icon-phone" d="M211 15 q-3 2 -1 8 q3 8 11 12 q5 2 7 -1 l-4 -4 q-2 2 -4 0 q-4 -3 -6 -7 q-1 -2 1 -3 z" fill="none" stroke="#fff" stroke-width="2.4" stroke-linejoin="round"/>
      <g class="icon-fax" fill="#fff"><rect x="261" y="14" width="12" height="6"/><rect x="257" y="21" width="20" height="10" rx="2"/><rect x="261" y="28" width="12" height="8" stroke="var(--teal)" stroke-width="1.5"/></g>
      <rect class="icon-mail" x="303" y="18" width="22" height="15" rx="2" fill="#fff"/>
      <path d="M303 19 l11 8 l11 -8" fill="none" stroke="var(--teal)" stroke-width="2"/>
      <circle class="icon-web" cx="363" cy="25" r="11" fill="#fff"/>
      <path d="M352 25 h22 M363 14 q-6 11 0 22 q6 -11 0 -22" fill="none" stroke="var(--teal)" stroke-width="2"/>
    </svg>

    <div class="line contact-list">
      203-555-0143<br>
      203-555-0187<br>
      dale@campwillowbrook.example<br>
      www.campwillowbrook.example
    </div>

    <svg class="divider divider--address" viewBox="0 0 567 50" aria-hidden="true">
      <g stroke="var(--teal)" stroke-width="3" stroke-linecap="round">
        <line x1="26" y1="25" x2="248" y2="25"/>
        <line x1="318" y1="25" x2="541" y2="25"/>
      </g>
      <circle cx="283" cy="25" r="21" fill="var(--teal)"/>
      <path class="icon-pin" d="M283 37 q-9 -10 -9 -17 a9 9 0 0 1 18 0 q0 7 -9 17 z" fill="#fff"/>
      <circle cx="283" cy="20" r="3.5" fill="var(--teal)"/>
    </svg>

    <div class="line address">
      Camp Willow Brook Charitable<br>
      Foundation, Inc PO Box<br>
      918 Alder Falls, VT 06832
    </div>

    <div class="line tagline">A camp where brave young hearts find joy...</div>
  </div>
</div>
</body>
</html>
```